Label Design for Climbing Chalk (fitness category)

I am looking for someone to design a front and back label for a bottle of liquid chalk. Liquid chalk is used in gyms, gymnastics, climbing to prevent your hands from getting moist and increase friction. I'm uploading some design motivations that I like.

The bottle is going to be black and I want the label to be clear. You have free reign of how you want to approach this design. Below are more specifics for the sizing:

*Attached is a picture of a competitor product (Tor Hold Liquid Chalk). Please don't use this for motivation, their label is very bad. I'm attaching a picture so that you can see what the bottle looks like.
*Attached are design motivations that I like
*The bottle is 50 ml, it's 3.75 inches tall, 2 inches wide and 1.25 inches in depth.
*The label can be square or oval (it's up to you). The size of the label needs to be 1,25 x 2.25 inches.
*Name of the product: Varnel Liquid Chalk
*Label needs to have the following Required Text. You can arrange it however you like:
- (50 ml)
- Made by USA Competitive Athletes for Athletes. Increases grip and lasts 3-4 times longer than regular chalk.
- Directions: Shake well. Squeeze some Varnel Liquid Chalk into your hand and rub your hands together. Let your hands air dry for about 10 seconds. To remove the chalk wash your hands with light soap.
Warning: Avoid contact with Eyes. Do not use on broken skin. Do not ingest. Keep out of reach of small children.
- Ingredients: Magnesium carbonate, SD Alcohol, hydroxypropylcellulose, colophonium.

Target Market(s)

Fitness, Athletes, Rock Climbers, Weight Lifters, Gymnasts, etc

Industry/Entity Type

Fitness

Font styles to use
Sans Serif

Colors

Designer to choose colors to be used in the design.

Requirements
Must have
• Please see Project Description for required text. The bottle is going to be black and I want the clear label so please be creative with the colors that would look good
Nice to have
• Please see attached branding ideas that I liked for font and colors. You don't have to strictly stick to them, these are just some of the ones I liked. Be creative and put your best foot forward.

```html
<!DOCTYPE html>
<html lang="en">
<head>
<meta charset="utf-8">
<title>Varnel Liquid Chalk – Front and Back Labels</title>
<link rel="stylesheet" href="https://fonts.googleapis.com/css2?family=Roboto+Condensed:wght@700&family=Nunito+Sans:ital,wght@0,400;0,700;1,400;1,800&display=swap">
<style>
  :root {
    --teal: #1b5c6b;
    --label-fill: #f3f5f7;
    --paper: #ffffff;
    --ink: #111111;
    --alert: #c8262b;
    --on-teal: #ffffff;
  }
  * { margin: 0; padding: 0; box-sizing: border-box; }
  html, body {
    width: 1200px; height: 1029px; overflow: hidden;
    background: var(--paper);
  }
  .canvas { position: relative; width: 1200px; height: 1029px; }
  .label-shapes {
    position: absolute; left: 0; top: 0;
    filter: drop-shadow(6px 14px 14px rgba(0,0,0,0.45));
  }
  .text-block { position: absolute; text-align: center; white-space: nowrap; }
  .front { left: 146px; width: 436px; }
  .back { left: 626px; width: 438px; }

  .brand-name {
    font-family: "Roboto Condensed", sans-serif;
    font-weight: 700;
    color: var(--teal);
  }
  .front-brand { top: 252px; font-size: 104px; line-height: 110px; }
  .back-brand { top: 216px; font-size: 80px; line-height: 80px; }

  .product-title {
    font-family: "Roboto Condensed", sans-serif;
    font-weight: 700;
    color: var(--ink);
    text-transform: uppercase;
  }
  .front-title {
    top: 464px; font-size: 52px; line-height: 56px;
    -webkit-text-stroke: 8px var(--label-fill);
    paint-order: stroke fill;
    text-shadow: 0 0 3px var(--label-fill);
  }
  .back-title { top: 319px; font-size: 46px; line-height: 46px; }

  .claim {
    top: 668px;
    font-family: "Nunito Sans", sans-serif;
    font-style: italic;
    font-size: 17.5px; line-height: 21px;
    letter-spacing: 1.2px;
    color: var(--on-teal);
  }
  .volume {
    top: 807px;
    font-family: "Nunito Sans", sans-serif;
    font-style: italic;
    font-size: 32px; line-height: 36px;
    letter-spacing: 1px;
    color: var(--on-teal);
  }

  .usage {
    position: absolute; left: 682px; top: 385px; width: 340px;
    font-family: "Nunito Sans", sans-serif;
    font-size: 17.5px; line-height: 24px;
    letter-spacing: 1.1px;
    color: var(--ink);
    white-space: nowrap;
  }
  .usage-heading {
    font-size: 22px; font-weight: 800; font-style: italic;
    color: var(--alert); letter-spacing: 0.5px;
  }
  .usage-heading.warning { margin-top: 18px; }

  .ingredients {
    top: 730px;
    font-family: "Nunito Sans", sans-serif;
    font-style: italic;
    font-size: 17.5px; line-height: 24px;
    color: var(--ink);
  }
  .ingredients-heading { font-weight: 800; font-size: 19px; }
</style>
</head>
<body>
<main class="canvas">
  <svg class="label-shapes" width="1200" height="1029" viewBox="0 0 1200 1029">
    <g class="front-label">
      <rect x="146" y="134" width="436" height="786" rx="218" fill="var(--paper)"/>
      <rect x="152" y="142" width="422" height="770" rx="211" fill="var(--teal)"/>
      <rect x="182" y="172" width="364" height="712" rx="182" fill="var(--label-fill)"/>
      <path role="img" aria-label="Teal open hand illustration"
            d="M205 530 Q205 400 300 400 L430 400 Q525 400 525 530 L525 640 Q515 760 460 842 Q365 876 270 842 Q215 760 205 640 Z"
            fill="var(--teal)"/>
    </g>
    <g class="back-label">
      <rect x="626" y="148" width="438" height="780" rx="219" fill="var(--paper)"/>
      <rect x="634" y="152" width="422" height="766" rx="211" fill="var(--teal)"/>
      <rect x="662" y="184" width="366" height="704" rx="183" fill="var(--paper)"/>
      <rect class="divider" x="711" y="699" width="274" height="8" fill="var(--teal)"/>
    </g>
  </svg>

  <div class="text-block front brand-name front-brand">Varnel</div>
  <h1 class="text-block front product-title front-title">Liquid Chalk</h1>
  <p class="text-block front claim">Made by USA Competitive<br>Athletes for Athletes.<br>Increases grip and lasts<br>3-4 times longer than<br>regular chalk.</p>
  <p class="text-block front volume">50 ml</p>

  <div class="text-block back brand-name back-brand">Varnel</div>
  <h2 class="text-block back product-title back-title">Liquid Chalk</h2>
  <section class="usage">
    <h3 class="usage-heading">Directions:</h3>
    <p>Shake well. Squeeze some Varnel<br>Liquid Chalk into your hand and rub<br>your hands together. Let your hands<br>air dry for about 10 seconds. To<br>remove the chalk wash your hands<br>with light soap.</p>
    <h3 class="usage-heading warning">Warning:</h3>
    <p>Avoid contact with Eyes. Do not use<br>on broken skin. Do not ingest. Keep<br>out of reach of small children.</p>
  </section>
  <section class="text-block back ingredients">
    <h3 class="ingredients-heading">Ingredients:</h3>
    <p>Magnesium carbonate, SD Alcohol,<br>hydroxypropylcellulose,<br>colophonium.</p>
  </section>
</main>
</body>
</html>
```